Business Card

Hello! We need a business card for a kid's ski shop in Vail, CO. During the Fall/Winter months, we are primarily a children's ski outfitter; however, we also carry many high end boutique items. Our age ranges are from Birth to about age 15. Our clientele come from all over the world. We would like a business card that is timeless, but fun considering we are a children's store. We have a large web presence and are really trying to brand our website www.TotTrailhub.com. Since we have such a tourist clientele, we try to remind them that they can shop 365 at our website. I have attached our new logos. Here is our store info:
PipTrek
418 W. Birch Ln., Suite F7
Vail, CO 81657
970-528-3094
www.TotTrailhub.com

```html
<!DOCTYPE html>
<html lang="en">
<head>
<meta charset="utf-8">
<title>PipTrek Business Card</title>
<link rel="stylesheet" href="https://fonts.googleapis.com/css2?family=Exo+2:wght@400;600;800&family=Oswald:wght@500&display=swap">
<style>
  :root {
    --stage: #e9e6e1;
    --card-red: #ff0a0a;
    --panel-light: #f7f7f7;
    --panel-shade: #d6d6d6;
    --ink-dark: #3a3a3a;
    --ink-mid: #555555;
    --white: #ffffff;
  }
  * { box-sizing: border-box; margin: 0; padding: 0; }
  html, body {
    width: 1200px; height: 1019px; overflow: hidden;
    background: var(--stage);
  }
  .stage {
    width: 1200px; height: 1019px;
    display: flex; align-items: center; justify-content: center;
  }
  .card {
    width: 900px; height: 514px;
    background: var(--card-red);
    box-shadow: 0 14px 34px rgba(0,0,0,.28);
    display: flex; flex-direction: column;
    font-family: "Exo 2", sans-serif;
  }
  .card-top {
    height: 290px;
    background: radial-gradient(ellipse at 55% 45%, var(--panel-light) 0%, #ececec 45%, var(--panel-shade) 100%);
    display: flex; align-items: center; justify-content: space-between;
    padding: 0 70px 0 60px;
  }
  .brand { display: flex; align-items: center; gap: 14px; }
  .brand-mark { width: 22px; height: 22px; background: var(--card-red); }
  .brand-text { display: flex; flex-direction: column; }
  .brand-name {
    font-weight: 800; font-size: 64px; line-height: 1; color: var(--ink-dark);
  }
  .brand-place {
    font-weight: 600; font-size: 15px; letter-spacing: 1px; color: var(--card-red);
    text-align: right; margin-top: 4px;
  }
  .person { text-align: left; }
  .person-name {
    font-family: "Oswald", sans-serif; font-weight: 500;
    font-size: 46px; letter-spacing: 1px; color: var(--ink-dark); line-height: 1.05;
  }
  .person-role {
    font-size: 19px; letter-spacing: 2.5px; color: var(--ink-mid);
  }
  .card-bottom { flex: 1; padding: 22px 0 0; color: var(--white); }
  .labels { display: flex; align-items: center; gap: 18px; }
  .rule { height: 7px; background: var(--white); }
  .rule-start { width: 40px; }
  .rule-mid { flex: 1; }
  .rule-end { width: 40px; }
  .label {
    font-weight: 800; font-size: 30px; letter-spacing: 1px; line-height: 1;
  }
  .details {
    display: grid; grid-template-columns: 1fr 1fr 1fr;
    padding: 26px 40px 0 60px; gap: 20px;
    font-size: 19px; line-height: 1.45; letter-spacing: .5px;
  }
</style>
</head>
<body>
<main class="stage">
  <article class="card">
    <section class="card-top">
      <div class="brand">
        <span class="brand-mark"></span>
        <div class="brand-text">
          <span class="brand-name">PipTrek</span>
          <span class="brand-place">ALDER RIDGE, NORTHPEAK</span>
        </div>
      </div>
      <div class="person">
        <p class="person-name">OWEN HALE</p>
        <p class="person-role">GENERAL MANAGER</p>
      </div>
    </section>
    <section class="card-bottom">
      <div class="labels">
        <span class="rule rule-start"></span>
        <span class="label">ADDRESS</span>
        <span class="rule rule-mid"></span>
        <span class="label">PHONE</span>
        <span class="rule rule-mid"></span>
        <span class="label">EMAIL</span>
        <span class="rule rule-end"></span>
      </div>
      <div class="details">
        <p class="detail-address">418 W. Birch Ln., Suite F7<br>Alder Ridge, NP 80110</p>
        <p class="detail-phone">970-528-3094<br>970-528-3094</p>
        <p class="detail-email">hello@piptrek.com<br>www.TotTrailhub.com</p>
      </div>
    </section>
  </article>
</main>
</body>
</html>
```